Real Estate "For Sale" Sign for construction company

We need a sign that we can use to hang on a post and place on the road when we sell a property. The sign will be simple and will need to mainly feature our logo (files attached), as well as the words "For Sale", and then our phone number "(555) 617 3489". The sign will hang on a post that'll look something like the attached picture.

Target Market(s)

Home buyers

Industry/Entity Type

Real Estate

Font styles to use
Serif
Sans Serif

Colors
0054AA
0677BA
7BADD7
CADEEF
E8F1F8
0094D4
00A9DD
6FCCEA
C7EBF8
E9F6FB

Requirements
Must have
• For Sale & our phone number

```html
<!DOCTYPE html>
<html lang="en">
<head>
<meta charset="utf-8">
<title>For Sale Sign</title>
<link rel="stylesheet" href="https://fonts.googleapis.com/css2?family=Montserrat:wght@400;500;700;800&display=swap">
<style>
  :root {
    --canvas-bg: #eef2f5;
    --sign-bg: #8fd8f7;
    --sign-rule: #ffffff;
    --navy: #141f4d;
    --brand-blue: #1b7fc4;
  }
  * { margin: 0; padding: 0; box-sizing: border-box; }
  html, body {
    width: 1200px;
    height: 1176px;
    overflow: hidden;
    background: var(--canvas-bg);
  }
  .sign {
    position: absolute;
    left: 208px;
    top: 38px;
    width: 784px;
    height: 1100px;
    background: var(--sign-bg);
    font-family: "Montserrat", Arial, sans-serif;
  }
  .sign-frame {
    position: absolute;
    inset: 20px;
    border: 2px solid var(--sign-rule);
  }
  .brand-name {
    position: absolute;
    left: 0;
    right: 0;
    top: 240px;
    text-align: center;
    font-weight: 500;
    font-size: 48px;
    color: var(--brand-blue);
    letter-spacing: 0.5px;
  }
  .sale-band {
    position: absolute;
    left: 0;
    right: 0;
    top: 469px;
    height: 209px;
    background: var(--navy);
    display: flex;
    align-items: center;
    justify-content: center;
  }
  .sale-title {
    font-weight: 800;
    font-size: 134px;
    line-height: 1;
    color: var(--sign-bg);
    letter-spacing: 2px;
  }
  .contact {
    position: absolute;
    left: 0;
    right: 0;
    top: 760px;
    text-align: center;
    color: var(--navy);
  }
  .contact-label {
    font-weight: 400;
    font-size: 54px;
    letter-spacing: 2px;
    line-height: 1.1;
  }
  .contact-phone {
    margin-top: 14px;
    font-weight: 700;
    font-size: 80px;
    line-height: 1.1;
  }
</style>
</head>
<body>
  <div class="sign">
    <div class="sign-frame"></div>
    <div class="brand-name">Stillwater Ridge Homes</div>
    <div class="sale-band">
      <div class="sale-title">FOR SALE</div>
    </div>
    <div class="contact">
      <div class="contact-label">CALL OR TEXT</div>
      <div class="contact-phone">(555) 617 3489</div>
    </div>
  </div>
</body>
</html>
```